Corvanta Inc Whitepaper

We need a word document redesigned for an upcoming crowdsale. The information for the crowdsale is complete, however we require some additional information being created in the form of infographics and custom images. I've uploaded 2 whitepapers with which to draw an idea of what we're trying to create. Included is an audit from our advisor of what else he thinks we need to create the finished product. Please follow his instructions as much as possible. Images from our game have also been provided which could possibly be used. If you require any further information please ask.

```html
<!DOCTYPE html>
<html lang="en">
<head>
<meta charset="utf-8">
<title>Corvanta Inc Whitepaper – Page Layouts</title>
<link href="https://fonts.googleapis.com/css2?family=Poppins:ital,wght@0,300;0,400;0,500;0,600;1,300;1,400&display=swap" rel="stylesheet">
<style>
  :root {
    --stage: #000000;
    --lime: #93c41c;
    --teal: #12a687;
    --paper: #ffffff;
    --heading-green: #3aa53a;
    --body-grey: #7a7a7a;
    --white: #ffffff;
    --art-warm: #c9a24a;
    --art-violet: #5b4a7c;
    --art-dark: #2a2630;
  }
  * { box-sizing: border-box; margin: 0; padding: 0; }
  html, body {
    width: 1200px; height: 578px; overflow: hidden;
    background: var(--stage);
    font-family: "Poppins", sans-serif;
  }
  .canvas { position: relative; width: 1200px; height: 578px; }

  .page {
    position: absolute; top: 15px; width: 366px; height: 534px;
    background: var(--paper); overflow: hidden;
  }
  .page--cover { left: 18px; }
  .page--inner { left: 411px; }
  .page--feature { left: 803px; }

  .brand-gradient { background: linear-gradient(90deg, var(--lime) 0%, var(--teal) 100%); }

  /* Cover */
  .page--cover {
    background: linear-gradient(100deg, var(--lime) 0%, #52b64a 50%, var(--teal) 100%);
    text-align: center; color: var(--white);
  }
  .cover-mark {
    position: absolute; left: 0; right: 0; top: 150px;
    display: flex; flex-direction: column; align-items: center; gap: 16px;
  }
  .cover-mark .dot {
    width: 88px; height: 88px; border-radius: 50%;
    background: rgba(255,255,255,0.9);
  }
  .cover-mark .name { font-size: 28px; font-weight: 600; color: var(--white); line-height: 1; }
  .cover-title { position: absolute; left: 0; right: 0; top: 306px; font-size: 21px; font-weight: 600; line-height: 30px; }
  .cover-sub { position: absolute; left: 0; right: 0; top: 345px; font-size: 16px; font-weight: 400; line-height: 22px; }

  /* Corner brand */
  .corner-brand {
    position: absolute; top: 10px; right: 10px;
    display: flex; flex-direction: column; align-items: center; gap: 3px;
  }
  .corner-brand .dot { width: 24px; height: 24px; border-radius: 50%; background: rgba(255,255,255,0.9); }
  .corner-brand .name { font-size: 9px; font-weight: 600; color: var(--white); }

  /* Header band */
  .page-header { position: absolute; left: 0; top: 0; width: 100%; height: 58px; color: var(--white); }
  .page-header h1 { position: absolute; left: 15px; top: 12px; font-size: 16px; font-weight: 600; line-height: 20px; }
  .page-header p { position: absolute; left: 15px; top: 34px; font-size: 12px; font-weight: 400; line-height: 16px; }

  /* Footer band */
  .page-footer {
    position: absolute; left: 0; bottom: 0; width: 100%; height: 24px;
    color: var(--white); font-size: 8px; font-weight: 500; letter-spacing: 0.4px;
  }
  .page-footer .site { position: absolute; left: 10px; top: 7px; }
  .page-footer .num { position: absolute; left: 182px; top: 7px; }
  .page-footer .dot {
    position: absolute; right: 8px; top: 3px; width: 18px; height: 18px;
    border-radius: 50%; background: rgba(255,255,255,0.9);
  }

  .para-title { color: var(--heading-green); font-weight: 500; letter-spacing: 0.6px; }
  .para-body {
    color: var(--body-grey); font-weight: 300;
    text-align: justify; hyphens: auto;
  }
  .para-body--wide { font-size: 7.9px; line-height: 12.6px; letter-spacing: 0.5px; }
  .para-body--narrow { font-size: 7.4px; line-height: 12.7px; letter-spacing: 0.4px; }

  /* Inner page */
  .intro-title { position: absolute; left: 17px; top: 75px; font-size: 10.5px; line-height: 15px; }
  .intro-body { position: absolute; left: 17px; top: 92px; width: 331px; }
  .column-title { position: absolute; left: 17px; top: 194px; font-size: 8.4px; line-height: 12px; }
  .column-body { position: absolute; left: 17px; top: 209px; width: 151px; }
  .game-art {
    position: absolute; left: 187px; top: 198px; width: 163px; height: 288px;
    background: radial-gradient(circle at 40% 30%, #e8c86a 0%, var(--art-warm) 22%, var(--art-violet) 55%, var(--art-dark) 100%);
  }

  /* Feature page */
  .feature-hero {
    position: absolute; left: 0; top: 0; width: 100%; height: 258px;
    background: linear-gradient(100deg, var(--lime) 0%, #5ab84a 50%, var(--teal) 100%);
  }
  .feature-quote {
    position: absolute; left: 18px; top: 146px; width: 330px;
    color: var(--white); font-size: 11.6px; font-style: italic; font-weight: 400;
    line-height: 15.7px; letter-spacing: 0.7px;
  }
  .feature-title { position: absolute; left: 18px; top: 281px; font-size: 10.5px; line-height: 15px; }
  .feature-body { position: absolute; left: 18px; top: 297px; width: 331px; }
</style>
</head>
<body>
<main class="canvas">

  <section class="page page--cover">
    <div class="cover-mark">
      <span class="dot"></span>
      <span class="name">Corvanta Inc</span>
    </div>
    <h1 class="cover-title">PROJECT TITLE HERE</h1>
    <p class="cover-sub">Subtext here</p>
  </section>

  <section class="page page--inner">
    <header class="page-header brand-gradient">
      <h1>PROJECT TITLE HERE</h1>
      <p>Subtext here</p>
      <div class="corner-brand"><span class="dot"></span><span class="name">Corvanta Inc</span></div>
    </header>

    <h2 class="para-title intro-title">Paragraph Title Here</h2>
    <p class="para-body para-body--wide intro-body">Lorem Ipsum is simply dummy text of the printing and typesetting industry. Lorem Ipsum has been the industry's standard dummy text ever since the 1500s, when an unknown printer took a galley of type and scrambled it to make a type specimen book. It has survived not only five centuries, but also the leap into electronic typesetting, remaining essentially unchanged. It was popularised in the 1960s with the release of Letraset sheets containing Lorem Ipsum passages, and more recently with desktop</p>

    <h3 class="para-title column-title">Paragraph Title Here</h3>
    <p class="para-body para-body--narrow column-body">Lorem Ipsum is simply dummy text of the printing and typesetting industry. Lorem Ipsum has been the industry's standard dummy text ever since the 1500s, when an unknown printer took a galley of type and scrambled it to make a type specimen book. It has survived not only five centuries, but also the leap into electronic typesetting, remaining essentially unchanged. It was popularised in the 1960s with the release of Letraset sheets containing Lorem Ipsum passages, and more recently with desktop five centuries, but also the leap into electronic typesetting, remaining essentially unchanged. It was popularised in the 1960s with the release of Letraset sheets containing Lorem Ipsum passages, and more recently with desktop</p>

    <div class="game-art" role="img" aria-label="Game artwork illustration"></div>

    <footer class="page-footer brand-gradient">
      <span class="site">WWW.CORVANTAINC.COM</span>
      <span class="num">PAGE: 01</span>
      <span class="dot"></span>
    </footer>
  </section>

  <section class="page page--feature">
    <div class="feature-hero">
      <div class="corner-brand"><span class="dot"></span><span class="name">Corvanta Inc</span></div>
      <p class="feature-quote">Lorem Ipsum is simply dummy text of the printing and typesetting industry. Lorem Ipsum has been the industry's standard dummy text ever since the 1500s, when an unknown printer took a galley of type and scrambled it to make a type specimen book. It has survived not only five</p>
    </div>

    <h2 class="para-title feature-title">Paragraph Title Here</h2>
    <p class="para-body para-body--wide feature-body">Lorem Ipsum is simply dummy text of the printing and typesetting industry. Lorem Ipsum has been the industry's standard dummy text ever since the 1500s, when an unknown printer took a galley of type and scrambled it to make a type specimen book. It has survived not only five centuries, but also the leap into electronic typesetting, remaining essentially unchanged. It was popularised in the 1960s with the release of Letraset sheets containing Lorem Ipsum passages, and more recently with desktop Lorem Ipsum has been the industry's standard dummy text ever since the 1500s, when an unknown printer took a galley of type and scrambled it to make a type specimen book. It has survived not only five centuries, but also the leap into electronic typesetting, remaining essentially unchanged. It was popularised in the 1960s with the release of Letraset sheets containing Lorem Ipsum passages, and more recently with desktop but also the leap into electronic typesetting, remaining essentially unchanged. It was popularised in the 1960s with the release of Letraset sheets containing Lorem Ipsum passages, and more recently</p>

    <footer class="page-footer brand-gradient">
      <span class="site">WWW.CORVANTAINC.COM</span>
      <span class="num">PAGE: 01</span>
      <span class="dot"></span>
    </footer>
  </section>

</main>
</body>
</html>
```